Manufacturing company needs new business card.

I need a unique Business Card that will truly stand out. Nothing too busy. Simple is good, right? Not looking for a standard design either. No cookie cutter layout. I am just looking for something interesting and a bit different. Does't have to completely off the wall crazy, just not your run of the mill business card. Clean and modern with a touch of industrial.

Target Market(s)

Air conditioning industry, Architects, builders.

Industry/Entity Type

Business

Contact Information for Business Card

Details to be included on card are:

Peter Vance
Managing Director

T: 1300 847 519
M: 0428 593 174
W: www.brenvaleworks.com.au
E: peter.vance@brenvaleworks.com.au
A: 58 Harwick Lane, Sydney NSW 2000

Font styles to use
Sans Serif

Colors
0355a3
848484
fbfbfb

Requirements
Must have
• Card design must be landscape.

```html
<!DOCTYPE html>
<html lang="en">
<head>
<meta charset="utf-8">
<title>Brenvale Works Australia – Business Card</title>
<link rel="stylesheet" href="https://fonts.googleapis.com/css2?family=Lato:wght@400;700&display=swap">
<style>
  :root {
    --brand-blue: #0355a3;
    --brand-grey: #848484;
    --paper: #fbfbfb;
    --backdrop: #dcdcdc;
    --text-font: "Lato", sans-serif;
  }
  * { box-sizing: border-box; margin: 0; padding: 0; }
  html, body { width: 1200px; height: 900px; overflow: hidden; }
  body {
    position: relative;
    background: var(--backdrop);
    font-family: var(--text-font);
    color: var(--brand-blue);
  }

  .card {
    position: absolute;
    width: 687px;
    height: 403px;
    background: var(--paper);
    overflow: hidden;
  }
  .band { position: absolute; left: 0; width: 100%; }
  .band--grey { background: var(--brand-grey); }
  .band--blue { background: var(--brand-blue); }

  /* Card back */
  .card--back { left: 124px; top: 118px; }
  .card--back .panel {
    position: absolute; left: 0; top: 25px; width: 100%; height: 304px;
    background: var(--brand-blue);
    border-radius: 0 22px 0 0;
  }
  .wordmark-plate {
    position: absolute; left: 115px; top: 110px; width: 460px; height: 102px;
    background: var(--paper); border-radius: 18px;
    display: flex; align-items: center; justify-content: center; gap: 18px;
  }
  .wordmark-plate .mark-square {
    width: 42px; height: 42px; background: var(--brand-blue);
  }
  .wordmark {
    font-family: var(--text-font);
    font-weight: 700;
    color: var(--brand-blue);
    white-space: nowrap;
  }
  .wordmark-plate .wordmark { font-size: 34px; }

  /* Card front */
  .card--front { left: 410px; top: 382px; height: 399px; }
  .header-band {
    position: absolute; left: 0; top: 28px; width: 100%; height: 53px;
    background: var(--brand-blue);
    display: flex; align-items: center; justify-content: flex-end; gap: 10px;
    padding-right: 12px;
  }
  .header-band .mark-square { width: 22px; height: 22px; background: var(--paper); }
  .header-band .wordmark { color: var(--paper); font-size: 19px; }

  .person {
    position: absolute; left: 0; top: 96px; width: 687px; text-align: center;
  }
  .person__name { font-size: 30px; font-weight: 400; letter-spacing: 0.5px; line-height: 1; }
  .person__role { font-size: 15px; font-weight: 700; margin-top: 6px; }

  .contact { position: absolute; font-size: 15.5px; white-space: nowrap; line-height: 1; }
  .contact--mobile { right: 469px; top: 200px; }
  .contact--tele   { right: 467px; top: 233px; }
  .contact--email  { left: 356px; top: 198px; display: flex; align-items: center; gap: 10px; }
  .contact--address{ left: 356px; top: 238px; display: flex; align-items: center; gap: 8px; }
  .contact svg { fill: var(--brand-blue); flex: none; }

  .website {
    position: absolute; left: 0; top: 354px; width: 100%; height: 20px;
    background: var(--brand-blue); color: var(--paper);
    font-size: 14px; text-align: center; line-height: 20px;
  }
</style>
</head>
<body>

  <section class="card card--back" aria-label="Card back">
    <div class="band band--grey" style="top:0;height:10px"></div>
    <div class="panel"></div>
    <div class="wordmark-plate">
      <span class="mark-square"></span>
      <span class="wordmark">Brenvale Works Australia</span>
    </div>
    <div class="band band--blue" style="top:340px;height:24px"></div>
    <div class="band band--blue" style="top:374px;height:13px"></div>
    <div class="band band--blue" style="top:395px;height:8px"></div>
  </section>

  <section class="card card--front" aria-label="Card front">
    <div class="band band--grey" style="top:0;height:15px"></div>
    <div class="header-band">
      <span class="mark-square"></span>
      <span class="wordmark">Brenvale Works Australia</span>
    </div>

    <div class="person">
      <h1 class="person__name">PETER VANCE</h1>
      <p class="person__role">Managing Director</p>
    </div>

    <p class="contact contact--mobile">Mobile: 0428 593 174</p>
    <p class="contact contact--tele">Tele: 1300 847 519</p>
    <p class="contact contact--email">
      <svg width="16" height="12" viewBox="0 0 16 12" aria-hidden="true"><path d="M0 0h16v12H0z M1 1l7 5 7-5" stroke="#fbfbfb" stroke-width="1.2"/></svg>
      peter.vance@brenvaleworks.com.au
    </p>
    <p class="contact contact--address">
      <svg width="14" height="19" viewBox="0 0 14 19" aria-hidden="true"><path d="M7 0a7 7 0 0 0-7 7c0 5 7 12 7 12s7-7 7-12a7 7 0 0 0-7-7zm0 10a3 3 0 1 1 0-6 3 3 0 0 1 0 6z"/></svg>
      58 Harwick Lane, Sydney NSW 2000
    </p>

    <div class="band band--blue" style="top:295px;height:43px"></div>
    <div class="website">www.brenvaleworks.com.au</div>
    <div class="band band--blue" style="top:383px;height:8px"></div>
  </section>

</body>
</html>
```